Harbor of Embers Label Redesign

We need our current label updated and to look more professional than it currently does. We feel the current image quality is too low and difficult to read. We like the theme of the label, but would like more gold on the label and the gold used to be metallic instead of a dull gold. Attached is our current label design and label on the bottle. We need all the information on it for legal labeling purposes, but please feel free to be creative with the layout and design. The message we want to convey is that this is a natural and luxury anti-aging skincare product. We feel our current label conveys natural, but needs to convey high end skincare more. Additionally, we want to see what the label looks like on the amber bottle with the gold lid image we uploaded.
Here are some of the improvements we would like to see:
-The border smaller and metallic (Shiny) gold
-All the gold shiny (Metallic)
-The print larger and clearer making it easier to read
-The label to not look so stretched out
Uploaded is the bottle we will be using, our logo, and the green leaf background. We also uploaded what we re currently using for comparison.
Target Market(s)
age 28+
Industry/Entity Type
beauty, skincare
Requirements
Must have
- Label information, metallic gold, easy to read

```html
<!DOCTYPE html>
<html lang="en">
<head>
<meta charset="utf-8">
<title>Harbor of Embers – Aging Defense Serum Label</title>
<link rel="stylesheet" href="https://fonts.googleapis.com/css2?family=Cinzel:wght@700;800&family=Lato:ital,wght@0,400;0,700;0,900;1,700;1,900&display=swap">
<style>
  :root {
    --page: #ffffff;
    --green-deep: #0a360d;
    --green-mid: #11501a;
    --green-light: #1a6a22;
    --leaf-1: #9fbf6a;
    --leaf-2: #4f7d33;
    --leaf-3: #2a5a1f;
    --gold-hi: #fff2a8;
    --gold: #e9c13d;
    --gold-mid: #c99a1e;
    --gold-low: #8a5f0c;
    --gold-text: #d8b25a;
    --ink-dark: #0f3311;
    --white: #ffffff;
  }
  * { margin: 0; padding: 0; box-sizing: border-box; }
  html, body {
    width: 1200px; height: 634px; overflow: hidden;
    background: var(--page);
  }
  .canvas { position: relative; width: 1200px; height: 634px; }

  .label {
    position: absolute; left: 42px; top: 37px; width: 1125px; height: 563px;
    overflow: hidden;
    background: radial-gradient(ellipse at 30% 35%, var(--green-light) 0%, var(--green-mid) 45%, var(--green-deep) 100%);
    font-family: "Lato", sans-serif;
  }

  .leaf-photo {
    position: absolute; left: 0; top: 300px; width: 560px; height: 250px;
    background:
      radial-gradient(ellipse at 48% 42%, var(--leaf-1) 0%, var(--leaf-2) 35%, var(--leaf-3) 70%, transparent 100%);
    opacity: .9;
  }

  /* brand */
  .brand { position: absolute; left: 112px; top: 62px; display: flex; align-items: center; gap: 18px; }
  .brand-dot { width: 96px; height: 96px; border-radius: 50%; background: var(--gold-mid); }
  .brand-name {
    font-family: "Lato", sans-serif; font-weight: 700; color: var(--gold);
    font-size: 54px; line-height: 1; letter-spacing: 2px;
  }
  .brand-name span { display: block; font-size: 24px; letter-spacing: 17px; margin-top: 12px; }

  /* title */
  .title {
    position: absolute; left: 0; width: 570px; top: 174px; text-align: center;
    font-family: "Cinzel", serif; font-weight: 800; font-size: 50px; line-height: 51px;
    background: linear-gradient(180deg, var(--gold-hi) 0%, var(--gold) 40%, var(--gold-mid) 65%, var(--gold-low) 100%);
    -webkit-background-clip: text; background-clip: text; color: transparent;
    filter: drop-shadow(0 2px 2px rgba(0,0,0,.6));
  }
  .subtitle {
    position: absolute; left: 0; width: 570px; top: 274px; text-align: center;
    font-weight: 900; font-style: italic; font-size: 25px; color: var(--gold);
    text-shadow: 0 2px 3px rgba(0,0,0,.6);
  }

  .actives {
    position: absolute; left: 54px; top: 336px; width: 466px; height: 42px;
    border: 2px solid var(--gold-hi); border-radius: 21px; padding: 3px;
  }
  .actives-inner {
    width: 100%; height: 100%; border: 2px solid var(--gold); border-radius: 17px;
    background: rgba(10, 40, 12, .85);
    display: flex; align-items: center; justify-content: center;
    color: var(--white); font-weight: 700; font-size: 15.5px;
  }

  .origin {
    position: absolute; left: 0; width: 570px; top: 398px; text-align: center;
    color: var(--ink-dark); font-weight: 700; font-size: 17px; line-height: 21px;
    text-shadow: 0 0 3px var(--white), 0 0 2px var(--white);
  }

  .net-wt {
    position: absolute; left: 146px; top: 512px; width: 278px; height: 32px;
    border-radius: 18px 18px 0 0;
    background: linear-gradient(180deg, var(--gold-hi), var(--gold) 45%, var(--gold-mid));
    display: flex; align-items: center; justify-content: center;
    color: var(--white); font-weight: 900; font-style: italic; font-size: 19px;
    -webkit-text-stroke: .8px var(--ink-dark);
  }

  .gold-band {
    position: absolute; left: 0; bottom: 0; width: 100%; height: 21px;
    background: linear-gradient(90deg, var(--gold-hi) 0%, var(--gold) 30%, var(--gold-mid) 60%, var(--gold-low) 85%, var(--gold-mid) 100%);
    border-top: 2px solid var(--white);
  }

  /* info column */
  .info { position: absolute; left: 617px; top: 59px; width: 470px; color: var(--gold-text); }
  .info-block { font-size: 16.8px; line-height: 19.6px; }
  .info-block + .info-block { margin-top: 16px; }
  .info h2 { font-size: 16.8px; font-weight: 700; line-height: 20px; margin-bottom: 1px; }
  .directions { margin-top: 17px !important; }
  .warnings { margin-top: 22px !important; }
  .maker { margin-top: 26px !important; }
  .maker p { line-height: 19px; }
</style>
</head>
<body>
<main class="canvas">
  <section class="label">
    <div class="leaf-photo" role="img" aria-label="Close-up photograph of a green leaf with water droplets"></div>

    <header class="brand">
      <div class="brand-dot"></div>
      <div class="brand-name">VERELLE<span>BOTANICS</span></div>
    </header>

    <h1 class="title">THE HARBOR<br>OF EMBERS</h1>
    <p class="subtitle">Aging Defense Serum</p>

    <div class="actives"><div class="actives-inner">Swiss Apple Stem Cells, Hyaluronic Acid, Retinol, Vitamin E</div></div>

    <p class="origin">MADE IN U.S.A.<br>Certified Organic and Natural Ingredients</p>

    <div class="net-wt">Net Wt: 1 oz/30 mL</div>
    <div class="gold-band"></div>

    <aside class="info">
      <div class="info-block ingredients">
        <h2>Ingredients:</h2>
        <p>Distilled Water, Organic Grape Seed Oil, Organic Jojoba Oil, Organic Avocado Oil, Organic Sunflower Oil, Tocopheryl Acetate (Vitamin E), CellVita™ Malus Domestica (Apple Stem Cell Extract), Hyaluronic Acid, Vitamin A (Retinol), Propylene Glycol, Essential Oil Blend (Tangerine, Lavender, Rosemary), Ethylhexylglycerine, Phenoxyethanol</p>
      </div>
      <div class="info-block directions">
        <h2>Directions:</h2>
        <p>Shake bottle prior to use as some separation may naturally occur. Apply generously to face, neck and back of hands morning/night. Can apply under make-up.</p>
      </div>
      <div class="info-block warnings">
        <h2>WARNINGS:</h2>
        <p>Keep out of eyes. External use only. Discontinue use if irritation occurs. Not intended for children. Consult with a Physician if pregnant, nursing or planning to become pregnant.</p>
      </div>
      <div class="info-block maker">
        <h2>Manufactured and Distributed by Verelle Botanics</h2>
        <p>P.O. Box 48152, Cedar Hollow, CO. 80577<br>www.VerelleBotanics.com</p>
      </div>
    </aside>
  </section>
</main>
</body>
</html>
```